Business Card Design Project

double sided, embossed, name & logo on front font sonsie one, back Name Maribel Stoddart, mobile 0468214093, Phone 76139584,
email maribel@brightwipe.com, use sysbols on the back for example an envelope for email, a telephone for phone number etc.symbol slate grey writing navy blue

Industry/Entity Type

Business

```html
<!DOCTYPE html>
<html lang="en">
<head>
<meta charset="utf-8">
<title>Bright Wipe – Business Card</title>
<link rel="stylesheet" href="https://fonts.googleapis.com/css2?family=Sonsie+One&family=Tinos&display=swap">
<style>
  :root {
    --backdrop: #b4c6c6;
    --card-light: #f4f4f4;
    --card-mid: #dcdcdc;
    --brand-blue: #1677d4;
    --icon-slate: #56646c;
  }
  * { margin: 0; padding: 0; box-sizing: border-box; }
  html, body {
    width: 1200px;
    height: 1139px;
    overflow: hidden;
    background: var(--backdrop);
  }
  .canvas {
    position: relative;
    width: 1200px;
    height: 1139px;
  }
  .card {
    position: absolute;
    width: 680px;
    height: 388px;
    overflow: hidden;
  }
  .card-texture {
    position: absolute;
    inset: 0;
    background: radial-gradient(ellipse at 55% 25%, var(--card-light) 0%, #e9e9e9 55%, var(--card-mid) 100%);
  }
  .card--front { left: 94px; top: 107px; }
  .card--back { left: 385px; top: 617px; }

  .holder-name {
    position: absolute;
    font-family: "Sonsie One", cursive;
    color: var(--brand-blue);
    font-size: 20px;
    white-space: nowrap;
  }
  .card--front .holder-name { right: 32px; top: 38px; }

  .brand-name {
    position: absolute;
    left: 48px;
    top: 175px;
    font-family: "Sonsie One", cursive;
    font-size: 46px;
    color: var(--brand-blue);
    white-space: nowrap;
  }

  .accent-bar {
    position: absolute;
    left: 0;
    top: 239px;
    width: 204px;
    height: 27px;
    background: var(--brand-blue);
  }
  .card--back .holder-name { left: 214px; top: 235px; }

  .contact-list {
    position: absolute;
    left: 214px;
    top: 272px;
    font-family: "Tinos", serif;
    font-size: 19px;
    color: var(--brand-blue);
    list-style: none;
  }
  .contact-row {
    display: flex;
    align-items: center;
    height: 36px;
  }
  .contact-item {
    display: flex;
    align-items: center;
    gap: 14px;
    margin-right: 18px;
  }
  .contact-icon { width: 32px; height: 26px; flex: none; }
  .contact-icon path, .contact-icon rect { fill: var(--icon-slate); }
</style>
</head>
<body>
<main class="canvas">

  <section class="card card--front" aria-label="Card front">
    <div class="card-texture" role="img" aria-label="Faint silver checkered card texture"></div>
    <p class="holder-name">Maribel Stoddart</p>
    <h1 class="brand-name">Bright Wipe</h1>
  </section>

  <section class="card card--back" aria-label="Card back">
    <div class="card-texture" role="img" aria-label="Faint silver checkered card texture"></div>
    <div class="accent-bar"></div>
    <p class="holder-name">Maribel Stoddart</p>
    <ul class="contact-list">
      <li class="contact-row">
        <span class="contact-item">
          <svg class="contact-icon" viewBox="0 0 32 26" aria-hidden="true">
            <path d="M1 3h30v20H1z M3.5 5v.6L16 14.5 28.5 5.6V5z M3.5 8.6V21h25V8.6L16 17.5z" fill-rule="evenodd"/>
          </svg>
          maribel@brightwipe.com
        </span>
      </li>
      <li class="contact-row">
        <span class="contact-item">
          <svg class="contact-icon" viewBox="0 0 32 26" aria-hidden="true">
            <path d="M11 0h10a2 2 0 0 1 2 2v22a2 2 0 0 1-2 2H11a2 2 0 0 1-2-2V2a2 2 0 0 1 2-2z M11 3v14h10V3z M14 20h4v3h-4z" fill-rule="evenodd"/>
          </svg>
          0468214093
        </span>
        <span class="contact-item">
          <svg class="contact-icon" viewBox="0 0 32 26" aria-hidden="true">
            <path d="M7 2l5 -1 3 7-3 3c1.5 4 4.5 7 8.5 8.5l3-3 7 3-1 5c-13 1-23.5-9.5-22.5-22.5z"/>
          </svg>
          76139584
        </span>
      </li>
    </ul>
  </section>

</main>
</body>
</html>
```